Security Company Needs a Website *

We need a website that gives our clients information about the services we provide, methods of contacting us and landing page to advertise on social media sites.

We need five landing pages titled Home, About Us, Services, Contact Us and a Landing Page that can be linked to Chatterloop advertising.

About Us - Should have a section for Core Values & Ethics, Our Vision, Our Mission and Partners.

Services - This page should show the different categories which include CCTV, Security Alarms, Access Control and Fire Protection.

CCTV Service Description:
Closed circuit television (CCTV) has long been implemented by businesses as a surveillance tool in areas that need monitoring. With digital CCTV cameras, multiple video cameras transmit signals through a set of monitors. The cameras provide thorough surveillance of the area.

With vast technological improvements over the last ten years, businesses with CCTV systems can use unique IP cameras and video analytics to monitor traffic flows, people-count, implement facial and number plate recognition. Useful information about customer behaviour and demographics can be discovered too. CCTV helps prevent crime in many industries and can assist with the improvement of industrial processes, safety on transport systems and traffic monitoring.

Security Alarms Service Description:
Alarms systems are electronic devices programmed to alert people to specific dangers and detect intrusions, fire or theft. Security alarms, systems and access control monitoring combine to create an integrated surveillance solution, tailored to your business’ unique requirements. Our surveillance and alarm monitoring services are ideal for perimeter protection from unwanted intruders or potential dangers.

Access Control Services:
An access control system allows for the free flow of authorised personnel while denying entry to unwanted visitors. With walk-in thieves and trespassers shut out, you dramatically reduce your exposure to crime while increasing the security of your employees, visitors, information and assets.

* Control when and who is entering your premises
* Protect employees, assets and information
* Secure an area or sector
* Observe movement
* Integrate with other security systems

Our range of access control systems can be seamlessly linked to other systems in our portfolio. These include Fire Detection Systems, Intruder Alarms, CCTV, and Building Management. A common request involves the need for a CCTV camera to pan around and focus on a door that has been highlighted as a security risk by the access control system.

Fire Protection Service:
To Be Advised

The above copy-writing will also have to be changed.

Contact Us - This form needs to be simple and straightforward to gather the prospects information and we would like to have a call to action on this page. The Contact Us page should also have a wayfindr charts location of our office address.

We would also like to have a link to our chatterloop page on the website.

Target Market(s)

Commercial businesses, building construction developers and property managers.

Industry/Entity Type

Security

Number of Pages Required

5+ page

Font styles to use
Sans Serif

Colors

Designer to choose colors to be used in the design.

Requirements
Must have
• We need to have the same look and feel as well as website features as the following website:
• https://www.kelvaguard.example.au/business-security/
• The website must be easy to use and easy to edit as well.

```html
<!DOCTYPE html>
<html lang="en">
<head>
<meta charset="utf-8">
<title>Lumenward Security — Exceeding Expectations</title>
<link href="https://fonts.googleapis.com/css2?family=Lato:wght@400;700;900&family=Open+Sans:wght@400;600;700&display=swap" rel="stylesheet">
<style>
:root{
  --navy:#1b2a78;
  --navy-deep:#121a55;
  --ink:#1e1e24;
  --body:#555a66;
  --muted:#777c88;
  --about-bg:#f3f5fb;
  --contact-bg:#e8ebf5;
  --footer-bg:#1c1f3d;
  --line:#9aa0b4;
  --white:#ffffff;
}
*{box-sizing:border-box;margin:0;padding:0}
html,body{width:1200px;height:3956px;overflow:hidden;background:var(--white)}
body{position:relative;font-family:"Open Sans",Arial,sans-serif;color:var(--body)}
.abs{position:absolute}
h1,h2,h3,.nav a,.btn{font-family:"Lato",Arial,sans-serif}

/* hero */
.hero{left:0;top:0;width:1200px;height:606px;overflow:hidden;
  background:linear-gradient(90deg,#eef2f2 0%,#f4f6f5 35%,#e9ecec 60%,#d9dcdc 100%)}
.hero-photo{left:0;top:0;width:1200px;height:606px;
  background:radial-gradient(ellipse 260px 320px at 880px 360px,#e7c7a8 0%,rgba(231,199,168,0) 70%),
             radial-gradient(ellipse 200px 130px at 830px 200px,#f7f8f6 0%,rgba(247,248,246,0) 80%),
             linear-gradient(90deg,rgba(140,175,150,.35) 0%,rgba(255,255,255,0) 30%)}
.brand{left:96px;top:12px;width:200px;text-align:center}
.brand-mark{width:122px;height:122px;border-radius:50%;background:var(--navy);margin:0 auto 6px}
.brand-name{font-family:"Lato",Arial,sans-serif;font-weight:700;font-size:17px;color:var(--navy-deep);line-height:1.05}
.brand-tag{font-family:"Lato",Arial,sans-serif;font-weight:700;font-size:10px;color:var(--navy-deep);letter-spacing:.3px}
.nav{left:556px;top:54px;display:flex;gap:34px}
.nav a{font-size:16px;font-weight:700;color:var(--ink);text-decoration:none;letter-spacing:.2px}
.nav a.active{color:var(--navy)}
.nav-icons{left:1016px;top:46px;display:flex;gap:14px}
.round{width:36px;height:36px;border-radius:50%;display:flex;align-items:center;justify-content:center}
.round.outline{border:2px solid var(--navy)}
.round.fill{background:var(--navy)}
.hero-kicker{left:98px;top:280px;font-size:29px;font-weight:400;color:var(--ink);letter-spacing:.5px}
.hero-title{left:98px;top:318px;font-size:42px;font-weight:700;color:var(--ink);letter-spacing:.3px}
.btn{display:inline-flex;align-items:center;justify-content:center;border:2px solid var(--navy);
  border-radius:30px;font-weight:700;color:var(--navy-deep);background:transparent;letter-spacing:.4px}
.hero-btn{left:98px;top:403px;width:176px;height:56px;font-size:15px}

/* about */
.about{left:0;top:606px;width:1200px;height:581px;background:var(--about-bg)}
.sec-title{width:1200px;text-align:center;font-size:36px;font-weight:700;color:var(--ink);letter-spacing:.5px}
.about-intro{left:220px;top:142px;width:760px;text-align:center;font-size:14px;line-height:28px;color:var(--muted)}
.pillar{width:260px;text-align:center}
.pillar-icon{width:169px;height:169px;border-radius:50%;margin:0 auto;
  background:radial-gradient(circle at 50% 30%,#2a3a9c 0%,var(--navy-deep) 75%);
  display:flex;align-items:center;justify-content:center}
.pillar h3{margin-top:34px;font-size:19px;font-weight:700;color:var(--ink)}
.pillar p{margin-top:12px;font-size:14px;line-height:22px;color:var(--muted)}

/* services */
.services-title{left:0;top:1254px}
.service h3{font-size:26px;font-weight:700;color:var(--ink)}
.service p,.service li{font-size:14px;line-height:26.5px;color:var(--body)}
.service ul{list-style:none}
.service .btn{width:138px;height:44px;font-size:13px;margin-top:32px}
.svc-img{border-radius:4px}
.img-camera{left:746px;top:1358px;width:256px;height:356px;
  background:linear-gradient(160deg,#d8d8d8 0%,#8e8e8e 45%,#2b2b2b 100%)}
.img-keypad{left:92px;top:1872px;width:396px;height:264px;
  background:linear-gradient(135deg,#f2f2f2 0%,#c9c9c9 55%,#8d8d8d 100%)}
.img-reader{left:722px;top:2358px;width:322px;height:326px;border-radius:14px;
  background:linear-gradient(135deg,#4a4a4a 0%,#2a2a2a 50%,#1a1a1a 100%)}
.img-detector{left:119px;top:2835px;width:395px;height:395px;border-radius:50%;
  background:radial-gradient(circle at 45% 45%,#ffffff 0%,#eeeeee 45%,#c9c9c9 80%,#a8a8a8 100%)}

/* contact */
.contact{left:0;top:3344px;width:1200px;height:527px;background:var(--contact-bg)}
.col-label{font-family:"Lato",Arial,sans-serif;font-size:19px;font-weight:700;color:var(--ink)}
.field{border:1px solid var(--line);background:transparent;font-size:12px;color:var(--muted);
  padding:0 10px;display:flex;align-items:center;height:32px}
.field.message{align-items:flex-start;padding-top:8px;height:82px}
.submit{left:633px;top:414px;width:92px;height:34px;border-radius:20px;background:var(--navy-deep);
  color:var(--white);font-family:"Lato",Arial,sans-serif;font-weight:700;font-size:13px;
  display:flex;align-items:center;justify-content:center;letter-spacing:.5px}
.info-row{display:flex;align-items:flex-start;gap:18px;font-size:13px;line-height:21px;color:var(--body)}
.info-icon{flex:0 0 34px;width:34px;height:34px;border-radius:50%;border:1px solid var(--line);
  display:flex;align-items:center;justify-content:center}
.social{display:flex;align-items:center;gap:12px;font-family:"Open Sans",Arial,sans-serif;
  font-size:14px;font-weight:600;color:var(--navy-deep)}
.social .dot{width:34px;height:34px;border-radius:50%;background:var(--navy)}

/* footer */
.footer{left:0;top:3871px;width:1200px;height:85px;background:var(--footer-bg);
  display:flex;align-items:center;justify-content:center;font-size:12px;color:#d8dbe8}
</style>
</head>
<body>

<header class="abs hero">
  <div class="abs hero-photo" role="img" aria-label="Photo of a hand pressing buttons on a wall-mounted alarm keypad"></div>
  <div class="abs brand">
    <div class="brand-mark"></div>
    <div class="brand-name">LUMENWARD SECURITY</div>
    <div class="brand-tag">EXCEEDING EXPECTATIONS</div>
  </div>
  <nav class="abs nav">
    <a class="active" href="#">HOME</a>
    <a href="#">ABOUT US</a>
    <a href="#">SERVICES</a>
    <a href="#">CONTACT US</a>
  </nav>
  <div class="abs nav-icons">
    <span class="round outline" aria-label="Search">
      <svg width="16" height="16" viewBox="0 0 16 16"><circle cx="6.5" cy="6.5" r="4.5" fill="none" stroke="#1b2a78" stroke-width="2"/><line x1="10" y1="10" x2="14" y2="14" stroke="#1b2a78" stroke-width="2.2" stroke-linecap="round"/></svg>
    </span>
    <span class="round fill" aria-label="Chatterloop"></span>
  </div>
  <h2 class="abs hero-kicker">LUMENWARD SECURITY</h2>
  <h1 class="abs hero-title">EXCEEDING EXPECTATIONS</h1>
  <span class="abs btn hero-btn">GET MORE INFO</span>
</header>

<section class="abs about">
  <h2 class="abs sec-title" style="left:0;top:76px">ABOUT US</h2>
  <p class="abs about-intro">Nemo enim ipsam voluptatem quia voluptas sit aspernatur aut odit aut fugit, sed quia consequuntur magni dolores eos qui ratione voluptatem sequi nesciunt neque porro quisquam est, qui dolorem ipsum quia dolor sit amet</p>

  <div class="abs pillar" style="left:70px;top:226px">
    <div class="pillar-icon">
      <svg width="80" height="70" viewBox="0 0 80 70" fill="none" stroke="#fff">
        <circle cx="30" cy="38" r="14" stroke-width="9" stroke-dasharray="5 4"/>
        <circle cx="30" cy="38" r="6" stroke-width="3"/>
        <circle cx="58" cy="20" r="9" stroke-width="6" stroke-dasharray="4 3"/>
        <circle cx="58" cy="20" r="3" stroke-width="2"/>
        <circle cx="60" cy="52" r="7" stroke-width="5" stroke-dasharray="3 3"/>
      </svg>
    </div>
    <h3>Core Values &amp; Ethics</h3>
    <p>Ut enim ad minima veniam, quis<br>nostrum exercitationem</p>
  </div>
  <div class="abs pillar" style="left:337px;top:226px">
    <div class="pillar-icon">
      <svg width="84" height="50" viewBox="0 0 84 50"><path d="M4 25 Q42 -12 80 25 Q42 62 4 25Z" fill="#fff"/><circle cx="42" cy="25" r="14" fill="#17226a"/><circle cx="42" cy="25" r="7" fill="#fff"/></svg>
    </div>
    <h3>Our Vision</h3>
    <p>Ut enim ad minima veniam, quis<br>nostrum exercitationem</p>
  </div>
  <div class="abs pillar" style="left:600px;top:226px">
    <div class="pillar-icon">
      <svg width="70" height="70" viewBox="0 0 70 70" fill="none" stroke="#fff"><circle cx="35" cy="35" r="30" stroke-width="6"/><circle cx="35" cy="35" r="17" stroke-width="6"/><circle cx="35" cy="35" r="6" fill="#fff" stroke="none"/></svg>
    </div>
    <h3>Our Mission</h3>
    <p>Ut enim ad minima veniam, quis<br>nostrum exercitationem</p>
  </div>
  <div class="abs pillar" style="left:867px;top:226px">
    <div class="pillar-icon">
      <svg width="84" height="64" viewBox="0 0 84 64" fill="#fff"><circle cx="42" cy="16" r="12"/><path d="M20 62 Q20 32 42 32 Q64 32 64 62Z"/><circle cx="16" cy="22" r="8"/><path d="M0 56 Q0 36 16 36 Q24 36 26 40 Q18 46 17 56Z"/><circle cx="68" cy="22" r="8"/><path d="M84 56 Q84 36 68 36 Q60 36 58 40 Q66 46 67 56Z"/></svg>
    </div>
    <h3>Partners</h3>
    <p>Ut enim ad minima veniam, quis<br>nostrum exercitationem</p>
  </div>
</section>

<main>
  <h2 class="abs sec-title services-title">SERVICES</h2>

  <article class="abs service" style="left:98px;top:1400px;width:520px">
    <h3>CCTV</h3>
    <p style="margin-top:26px">Closed circuit television (CCTV) has long been implemented by businesses as a surveillance tool in areas that need monitoring. With digital CCTV cameras, multiple video cameras transmit signals through a set of monitors. The cameras provide thorough surveillance of the area.With vast technological improvements over the last ten years, businesses with CCTV systems can use unique IP cameras and video analytics to monitor traffic flows, people-count, implement facial and number plate recognition.</p>
    <span class="btn">READ MORE</span>
  </article>
  <div class="abs svc-img img-camera" role="img" aria-label="Photo of a wall-mounted CCTV security camera"></div>

  <div class="abs svc-img img-keypad" role="img" aria-label="Photo of a security alarm control keypad"></div>
  <article class="abs service" style="left:604px;top:1852px;width:500px">
    <h3>Security Alarms</h3>
    <p style="margin-top:26px">Alarms systems are electronic devices programmed to alert people to specific dangers and detect intrusions, fire or theft. Security alarms, systems and access control monitoring combine to create an integrated surveillance solution, tailored to your business’ unique requirements. Our surveillance and alarm monitoring services are ideal for perimeter protection from unwanted intruders or potential dangers.</p>
    <span class="btn">READ MORE</span>
  </article>

  <article class="abs service" style="left:98px;top:2328px;width:520px">
    <h3>Access Control</h3>
    <p style="margin-top:26px">An access control system allows for the free flow of authorised personnel while denying entry to unwanted visitors. With walk-in thieves and trespassers shut out, you dramatically reduce your exposure to crime while increasing the security of your employees, visitors, information and assets.</p>
    <p style="margin-top:14px">Control when and who is entering your premises</p>
    <ul>
      <li>* Protect employees, assets and information</li>
      <li>* Secure an area or sector</li>
      <li>* Observe movement</li>
      <li>* Integrate with other security systems</li>
    </ul>
    <span class="btn" style="margin-top:30px">READ MORE</span>
  </article>
  <div class="abs svc-img img-reader" role="img" aria-label="Photo of a fingerprint access control terminal with keypad"></div>

  <div class="abs img-detector" role="img" aria-label="Photo of a white ceiling smoke detector"></div>
  <article class="abs service" style="left:604px;top:2882px;width:500px">
    <h3>Fire Protection</h3>
    <p style="margin-top:26px">Alarms systems are electronic devices programmed to alert people to specific dangers and detect intrusions, fire or theft. Security alarms, systems and access control monitoring combine to create an integrated surveillance solution, tailored to your business’ unique requirements. Our surveillance and alarm monitoring services are ideal for perimeter protection from unwanted intruders or potential dangers.</p>
    <span class="btn">READ MORE</span>
  </article>
</main>

<section class="abs contact">
  <h2 class="abs sec-title" style="left:0;top:76px">CONTACT US</h2>

  <div class="abs col-label" style="left:98px;top:158px">Contact form</div>
  <div class="abs field" style="left:98px;top:226px;width:311px">Name :</div>
  <div class="abs field" style="left:418px;top:226px;width:310px">Phone no :</div>
  <div class="abs field" style="left:98px;top:272px;width:630px">Email :</div>
  <div class="abs field message" style="left:98px;top:318px;width:630px">Message :</div>
  <div class="abs submit">SUBMIT</div>

  <div class="abs col-label" style="left:780px;top:158px">Contact Information</div>
  <div class="abs info-row" style="left:780px;top:210px;width:300px">
    <span class="info-icon"><svg width="12" height="16" viewBox="0 0 12 16"><path d="M6 0C2.7 0 0 2.6 0 5.9 0 10 6 16 6 16s6-6 6-10.1C12 2.6 9.3 0 6 0z" fill="#1b2a78"/><circle cx="6" cy="6" r="2.2" fill="#fff"/></svg></span>
    <span style="padding-top:2px">Nam libero tempore, cum soluta no<br>bis est eligendi optio</span>
  </div>
  <div class="abs info-row" style="left:780px;top:272px;width:300px">
    <span class="info-icon"><svg width="14" height="14" viewBox="0 0 14 14"><path d="M3 0l2.5 3.2-1.6 1.7c.9 2 2.3 3.5 4.3 4.4l1.7-1.6L13 10.2 11.3 13C5.5 12.7 1.3 8.5 1 2.7z" fill="#1b2a78"/></svg></span>
    <span style="padding-top:6px">1 800 555 0142</span>
  </div>
  <div class="abs info-row" style="left:780px;top:332px;width:300px">
    <span class="info-icon"><svg width="16" height="12" viewBox="0 0 16 12"><rect width="16" height="12" rx="1.5" fill="#1b2a78"/><path d="M1 1.5l7 5 7-5" fill="none" stroke="#fff" stroke-width="1.4"/></svg></span>
    <span style="padding-top:6px">info@lumenward.example</span>
  </div>
  <div class="abs col-label" style="left:780px;top:373px">Social Media</div>
  <div class="abs social" style="left:780px;top:418px"><span class="dot"></span>Chatterloop</div>
</section>

<footer class="abs footer">Copyright © 2018, Lumenward Security. All rights reserved.</footer>

</body>
</html>
```